Pebble Lantern Fine Chocolates
Handcrafted in Tucson, Arizona
Pebble Lantern Fine Chocolates -
Creative Brief
Customers who buy my chocolates or are interested in knowing more and purchasing them in the future. Foodies, Downtowners, Tucson tourists, students, coffee shop-types, mostly women.
they need to fit in a box that is 6 1/2 inches by 3 7/8 inches. Ideally, they will be approximately 4.5 inches by 13 3/4 inches, and then fold like an accordian 5 times to be 4.5 by 2 3/4 in your hand.

```html
<!DOCTYPE html>
<html lang="en">
<head>
<meta charset="utf-8">
<title>Pebble Lantern Fine Chocolates – Flavor Brochure</title>
<link rel="stylesheet" href="https://fonts.googleapis.com/css2?family=Playfair+Display:ital,wght@1,700&family=Questrial&display=swap">
<style>
  :root {
    --maroon: #6a1320;
    --cream: #fbf1d2;
    --cream-light: #fff8e4;
    --orange: #e0842a;
    --title: #7a1d24;
    --white: #ffffff;
  }
  * { margin: 0; padding: 0; box-sizing: border-box; }
  html, body { width: 1200px; height: 446px; overflow: hidden; background: var(--cream); }
  .brochure { position: relative; width: 1200px; height: 446px; overflow: hidden; background: var(--cream); font-family: "Questrial", sans-serif; }
  .backdrop { position: absolute; inset: 0; }
  .flavor-title { position: absolute; font-family: "Playfair Display", serif; font-weight: 700; font-style: italic; font-size: 36px; line-height: 1; color: var(--title); white-space: nowrap; }
  .flavor-title--orange { color: var(--orange); }
  .flavor-copy { position: absolute; font-size: 10px; line-height: 1.4; color: var(--orange); letter-spacing: 0.3px; }
  .logo-badge { position: absolute; left: 968px; top: 30px; width: 124px; height: 124px; border-radius: 50%; background: var(--cream-light); border: 3px solid var(--orange); display: flex; align-items: center; justify-content: center; text-align: center; }
  .logo-name { font-size: 14px; line-height: 1.25; color: var(--maroon); padding: 0 14px; }
  .website { position: absolute; left: 925px; top: 414px; font-size: 12px; color: var(--white); letter-spacing: 0.6px; }
</style>
</head>
<body>
<main class="brochure">
  <svg class="backdrop" width="1200" height="446" viewBox="0 0 1200 446">
    <defs>
      <radialGradient id="truffleTones" cx="50%" cy="45%" r="60%">
        <stop offset="0" stop-color="#8a4a36"/>
        <stop offset="0.55" stop-color="#4a2018"/>
        <stop offset="1" stop-color="#d9c6a0"/>
      </radialGradient>
      <linearGradient id="panelPhotoTones" x1="0" y1="0" x2="1" y2="1">
        <stop offset="0" stop-color="#f0d9c4"/>
        <stop offset="0.5" stop-color="#5a2418"/>
        <stop offset="1" stop-color="#2c2a44"/>
      </linearGradient>
    </defs>
    <path class="band-top" fill="var(--maroon)" d="M0,0 H920 V40 C800,70 700,10 560,14 C400,20 260,10 0,18 Z"/>
    <path class="band-bottom" fill="var(--maroon)" d="M0,446 V424 C200,414 420,440 640,428 C780,420 870,418 920,420 V446 Z"/>
    <path class="band-left" fill="var(--maroon)" d="M0,0 H10 C6,150 12,300 8,446 H0 Z"/>
    <path class="panel-right" fill="var(--maroon)" d="M912,0 H1200 V446 H912 C920,300 904,150 912,0 Z"/>
    <g class="photos">
      <circle cx="180" cy="112" r="68" fill="url(#truffleTones)" stroke="var(--cream-light)" stroke-width="3" role="img" aria-label="Photo of a La Brisa truffle topped with a rose petal"/>
      <circle cx="352" cy="320" r="60" fill="url(#truffleTones)" stroke="var(--cream-light)" stroke-width="3" role="img" aria-label="Photo of a Café Dorado chocolate with an orange top"/>
      <circle cx="566" cy="180" r="62" fill="url(#truffleTones)" stroke="var(--cream-light)" stroke-width="3" role="img" aria-label="Photo of a Desert Toffee chocolate"/>
      <circle cx="776" cy="190" r="66" fill="url(#truffleTones)" stroke="var(--cream-light)" stroke-width="3" role="img" aria-label="Photo of Arroz Dulce chocolates"/>
      <rect x="925" y="168" width="265" height="222" fill="url(#panelPhotoTones)" role="img" aria-label="Photo of a chocolate truffle with rose petal among blueberries"/>
      <ellipse cx="40" cy="380" rx="22" ry="34" fill="#e8c64a" opacity="0.75" role="img" aria-label="Yellow flower illustration"/>
    </g>
  </svg>

  <h2 class="flavor-title" style="left:290px; top:80px;">La Brisa</h2>
  <p class="flavor-copy" style="left:482px; top:20px; width:165px;">A dark chocolate truffle blended with sweet spice and a hint of chile, finished with a rose petal. Every bite is soft and lingering, made fresh in small batches.</p>

  <h2 class="flavor-title flavor-title--orange" style="left:70px; top:238px;">Café Dorado</h2>
  <p class="flavor-copy" style="left:90px; top:288px; width:178px;">The coffee lover's perfect bite, with a rich layer of organic espresso and desert honey folded into milk chocolate. Smooth, bold and a little sweet, it pairs well with your morning cup.</p>

  <h2 class="flavor-title" style="left:462px; top:252px;">Desert Toffee</h2>
  <p class="flavor-copy" style="left:470px; top:304px; width:220px;">Toffee like you love, with a taste of Tucson. Buttery crunch, toasted pecans and a touch of cinnamon under a coat of dark chocolate, a treat worth saving for last.</p>

  <p class="flavor-copy" style="left:712px; top:280px; width:190px;">A favorite Tucson drink becomes a creamy white chocolate ganache with rice, vanilla and cinnamon, dusted in cocoa and finished by hand.</p>
  <h2 class="flavor-title" style="left:730px; top:368px; font-size:32px;">Arroz Dulce</h2>

  <div class="logo-badge"><span class="logo-name">Pebble Lantern Fine Chocolates</span></div>
  <p class="website">pebblelanternchocolates.com</p>
</main>
</body>
</html>
```